Brevanta Interiors
Business Card, Stationery Package, Email Signature
Project: Brevanta Interiors
Brevanta Interiors -
Creative Brief
Professional
Marisol Pryde
Managing Director
P.O.Box 4372 Converse, TX 78109 - 4372
mpryde@brevantainteriors.example
www.brevantainteriors.example
Brevanta Interiors is a retail store offering Flooring products and Installation services. We would like to have the following items made: Business Card, Stationery Package (Fax, Letterhead, Envelopes, etc.), and Email Signature. We would like to see two types of fonts created for comparison, the original font and one of your own professional choices. Winner, please provide all design templates for future modification upon completion of the contest. Thank you!
logo, text, slogan, and web address.

```html
<!DOCTYPE html>
<html lang="en">
<head>
<meta charset="utf-8">
<title>Brevanta Interiors – Business Cards</title>
<link href="https://fonts.googleapis.com/css2?family=Open+Sans:ital,wght@0,400;0,600;0,700;1,400;1,700&display=swap" rel="stylesheet">
<style>
  :root {
    --backdrop: #e7e4df;
    --card: #ffffff;
    --navy: #1c2c86;
    --royal: #3564c9;
    --sky: #6f93dd;
    --leaf: #5fb536;
    --brand-blue: #1f4aa8;
    --ink: #3c3f4a;
    --rule: #9aa3b8;
    --icon: #3564c9;
    --ghost: #e6ecf4;
  }
  * { box-sizing: border-box; margin: 0; padding: 0; }
  html, body { width: 1200px; height: 852px; overflow: hidden; }
  body {
    background: var(--backdrop);
    font-family: "Open Sans", Arial, sans-serif;
    position: relative;
    color: var(--ink);
  }
  .card {
    position: absolute;
    width: 520px;
    height: 300px;
    background: var(--card);
    border-radius: 18px;
    overflow: hidden;
    box-shadow: 0 6px 18px rgba(0,0,0,0.18);
  }
  .card--classic { left: 60px; top: 90px; }
  .card--modern { left: 620px; top: 462px; }

  .band {
    position: absolute;
    left: 0; right: 0;
    top: 36px;
    height: 52px;
    background: linear-gradient(90deg, var(--navy) 0%, var(--royal) 45%, var(--sky) 70%, var(--royal) 100%);
    border-bottom: 4px solid var(--leaf);
  }
  .holder {
    position: absolute;
    right: 26px;
    top: 42px;
    text-align: right;
    color: #fff;
    line-height: 1.2;
  }
  .holder__name { font-weight: 700; font-size: 17px; }
  .holder__title { font-style: italic; font-size: 13px; }

  .brand-mark {
    position: absolute;
    left: 92px; top: 30px;
    width: 60px; height: 60px;
    border-radius: 50%;
    background: var(--leaf);
  }
  .brand-name {
    position: absolute;
    left: 18px; top: 100px;
    font-weight: 700;
    font-size: 31px;
    color: var(--brand-blue);
    letter-spacing: -0.5px;
  }

  .address {
    position: absolute;
    text-align: right;
    font-size: 12.5px;
    line-height: 1.55;
  }
  .card--classic .address { left: 90px; top: 196px; width: 150px; }
  .divider {
    position: absolute;
    left: 252px; top: 188px;
    width: 1px; height: 90px;
    background: var(--rule);
  }
  .contacts { position: absolute; list-style: none; font-size: 12.5px; }
  .card--classic .contacts { left: 264px; top: 186px; }
  .card--modern .contacts { left: 26px; top: 188px; }
  .contacts li { display: flex; align-items: center; gap: 7px; height: 21px; }
  .contacts svg { width: 14px; height: 14px; flex: none; }

  .card--modern .address { left: 26px; top: 160px; text-align: left; white-space: nowrap; }
  .ghost-mark {
    position: absolute;
    right: 58px; top: 160px;
    width: 110px; height: 110px;
    border-radius: 50%;
    background: var(--ghost);
  }
</style>
</head>
<body>

<svg width="0" height="0" style="position:absolute">
  <defs>
    <symbol id="icon-phone" viewBox="0 0 14 14">
      <rect x="3.5" y="0.5" width="7" height="13" rx="1.5" fill="var(--icon)"/>
      <rect x="5" y="2" width="4" height="5" fill="#fff"/>
    </symbol>
    <symbol id="icon-fax" viewBox="0 0 14 14">
      <rect x="3.5" y="0.5" width="7" height="5" fill="none" stroke="var(--icon)" stroke-width="1.2"/>
      <rect x="1" y="5" width="12" height="6" rx="1" fill="var(--icon)"/>
      <rect x="3.5" y="10" width="7" height="3.5" fill="var(--icon)"/>
    </symbol>
    <symbol id="icon-mail" viewBox="0 0 14 14">
      <circle cx="7" cy="7" r="6.5" fill="var(--icon)"/>
      <rect x="3.5" y="4.5" width="7" height="5" fill="#fff"/>
      <path d="M3.5 4.5 L7 7.5 L10.5 4.5" fill="none" stroke="var(--icon)" stroke-width="0.9"/>
    </symbol>
    <symbol id="icon-web" viewBox="0 0 14 14">
      <circle cx="7" cy="7" r="6" fill="none" stroke="var(--icon)" stroke-width="1.3"/>
      <ellipse cx="7" cy="7" rx="2.5" ry="6" fill="none" stroke="var(--icon)" stroke-width="1"/>
      <line x1="1" y1="7" x2="13" y2="7" stroke="var(--icon)" stroke-width="1"/>
    </symbol>
  </defs>
</svg>

<section class="card card--classic">
  <div class="band"></div>
  <div class="holder">
    <div class="holder__name">Marisol Pryde</div>
    <div class="holder__title">Managing Director</div>
  </div>
  <div class="brand-mark"></div>
  <div class="brand-name">Brevanta Interiors</div>

  <div class="address">P.O.Box 4372<br>Harlow Bend,<br>TX 70418 - 4372</div>
  <div class="divider"></div>
  <ul class="contacts">
    <li><svg><use href="#icon-phone"/></svg>210.555.0142</li>
    <li><svg><use href="#icon-fax"/></svg>210.555.0187</li>
    <li><svg><use href="#icon-mail"/></svg>mpryde@brevantainteriors.example</li>
    <li><svg><use href="#icon-web"/></svg>www.brevantainteriors.example</li>
  </ul>
</section>

<section class="card card--modern">
  <div class="band"></div>
  <div class="holder">
    <div class="holder__name">Marisol Pryde</div>
    <div class="holder__title">Managing Director</div>
  </div>
  <div class="brand-mark"></div>
  <div class="brand-name">Brevanta Interiors</div>
  <div class="ghost-mark"></div>

  <div class="address">P.O.Box 4372 Harlow Bend, TX 70418 - 4372</div>
  <ul class="contacts">
    <li><svg><use href="#icon-phone"/></svg>210.555.0142</li>
    <li><svg><use href="#icon-fax"/></svg>210.555.0187</li>
    <li><svg><use href="#icon-mail"/></svg>mpryde@brevantainteriors.example</li>
    <li><svg><use href="#icon-web"/></svg>www.brevantainteriors.example</li>
  </ul>
</section>

</body>
</html>
```